Article/Flyer - Reservation of Rights

We would like an article that we normally produce through illustrator in a pdf format to be placed in a Word format. We have provided a sample article/flyer of our normal distribution style. We would like the outcome to be in WORD format

```html
<!DOCTYPE html>
<html lang="en">
<head>
<meta charset="utf-8">
<title>Reservation of Rights Letter – Kestrel Risk Advisors</title>
<link rel="stylesheet" href="https://fonts.googleapis.com/css2?family=Open+Sans:wght@400;600&family=Oswald:wght@700&display=swap">
<style>
  :root {
    --brand-red: #a1303f;
    --ink: #2f2f2f;
    --wordmark: #2a2a2a;
    --footer-dark: #363636;
    --paper: #ffffff;
    --sky-light: #e6eef4;
    --sky-mid: #a9bfd1;
    --steel: #6f86a3;
  }
  * { box-sizing: border-box; margin: 0; padding: 0; }
  html, body { width: 848px; height: 1200px; overflow: hidden; background: var(--paper); }
  body { font-family: "Open Sans", Arial, sans-serif; color: var(--ink); }

  .flyer { position: relative; width: 848px; height: 1200px; overflow: hidden; background: var(--paper); }

  /* Header */
  .hero-image {
    position: absolute; left: 0; top: 0; width: 848px; height: 287px;
    background:
      linear-gradient(100deg, rgba(255,255,255,0.85) 0%, rgba(255,255,255,0.55) 38%, rgba(255,255,255,0) 55%),
      linear-gradient(180deg, var(--sky-light) 0%, var(--sky-mid) 45%, var(--steel) 100%);
  }
  .brand { position: absolute; left: 76px; top: 32px; width: 420px; }
  .brand-name {
    font-family: "Open Sans", Arial, sans-serif; font-weight: 600;
    font-size: 32px; line-height: 38px; color: var(--wordmark); white-space: nowrap;
  }
  .brand-tagline {
    font-size: 13px; line-height: 18px; color: var(--wordmark); margin-top: 4px; white-space: nowrap;
  }
  .brand-legal { font-size: 10px; color: #333; margin-top: 8px; white-space: nowrap; }

  /* Intro band */
  .intro-band {
    position: absolute; left: 0; top: 287px; width: 848px; height: 86px;
    background: var(--brand-red); padding: 7px 8px;
  }
  .intro-frame {
    height: 100%; border: 1.5px solid rgba(255,255,255,0.9);
    padding: 6px 24px 0 25px;
  }
  .intro-text { color: #fff; font-weight: 600; font-size: 13.6px; line-height: 21.5px; letter-spacing: 0.45px; }

  /* Section heading tabs */
  .section-tab { position: absolute; height: 41px; }
  .section-tab svg { position: absolute; left: 0; top: 0; }
  .section-tab h2 {
    position: relative; font-family: "Oswald", "Arial Narrow", sans-serif; font-weight: 700;
    font-size: 17px; line-height: 41px; color: #fff; letter-spacing: -0.2px; white-space: nowrap;
  }
  .tab-what { left: 0; top: 400px; width: 375px; }
  .tab-what h2 { padding-left: 20px; }
  .tab-interpret { left: 0; top: 823px; width: 254px; }
  .tab-interpret h2 { padding-left: 20px; }
  .tab-proceed { left: 596px; top: 745px; width: 252px; }
  .tab-proceed h2 { padding-left: 41px; }

  /* Body copy */
  .copy { position: absolute; font-size: 12.7px; line-height: 18.3px; text-align: justify; letter-spacing: 0.28px; }
  .copy p + p { margin-top: 11px; }
  .copy-what { left: 20px; top: 449px; width: 384px; }
  .copy-interpret { left: 20px; top: 879px; width: 390px; }
  .copy-interpret .lead-in { text-align: left; }
  .copy-right-top { left: 447px; top: 401px; width: 381px; }
  .copy-proceed { left: 452px; top: 808px; width: 378px; }

  /* Footer */
  .footer-band { position: absolute; left: 0; top: 1111px; width: 848px; height: 89px; }
  .footer-address {
    position: absolute; left: 0; top: 1111px; width: 848px; height: 36px;
    display: flex; align-items: center; justify-content: center; gap: 9px;
    color: #fff; font-weight: 600; font-size: 16.5px;
  }
  .footer-contacts {
    position: absolute; left: 0; top: 1147px; width: 848px; height: 36px;
    display: flex; align-items: center; color: #fff; font-weight: 600; font-size: 16px;
  }
  .contact { position: absolute; display: flex; align-items: center; gap: 7px; white-space: nowrap; }
  .contact-phone { left: 82px; }
  .contact-fax { left: 313px; }
  .contact-web { left: 543px; }
</style>
</head>
<body>
<main class="flyer">

  <header>
    <div class="hero-image" role="img" aria-label="Photo montage: city office tower, rolled certificate of insurance and a team of design professionals reviewing plans"></div>
    <div class="brand">
      <div class="brand-name">Kestrel Risk Advisors</div>
      <div class="brand-tagline">Serving Architects, Engineers and Environmental Consultants</div>
      <div class="brand-legal">Northbay Risk Partners, LLC dba Kestrel Risk Advisors</div>
    </div>
  </header>

  <section class="intro-band">
    <div class="intro-frame">
      <p class="intro-text">Reporting a claim or potential claim to your professional liability insurance company will trigger a fair amount of return correspondence that often creates confusion rather than clarity. One document that commonly falls into this category is the Reservation of Rights Letter.</p>
    </div>
  </section>

  <div class="section-tab tab-what">
    <svg width="375" height="41" viewBox="0 0 375 41"><polygon points="0,0 357,0 375,41 0,41" fill="var(--brand-red)"/></svg>
    <h2>WHAT IS THE RESERVATION OF RIGHTS LETTER</h2>
  </div>
  <article class="copy copy-what">
    <p>The Reservation of Rights Letter is a normal part of the insurance claims process. Its purpose is to provide notification from the insurance company to the policy holder that coverage may not apply. While this often comes as alarming news, the Reservation of Rights Letter should not be mistaken as an outright denial -- it does not automatically mean that coverage is being or will be denied.</p>
    <p>This standard correspondence is routinely sent to comply with state laws and preserve the insurance company’s legal ability to deny some, or all, of the claim pending further investigation while the claim is ongoing and being handled by the insurance company. Failure to send the letter could be considered a waiver of their rights at a later time.</p>
    <p>Because information is vague in the early stages of a claim and often is limited to unsubstantiated allegations and a few facts, the Reservation of Rights Letter protects the insurance company’s interests to later deny coverage in whole or part based on evidence revealed during claims handling.</p>
  </article>

  <div class="section-tab tab-interpret">
    <svg width="254" height="41" viewBox="0 0 254 41"><polygon points="0,0 236,0 254,20.5 236,41 0,41" fill="var(--brand-red)"/></svg>
    <h2>INTERPRETING THE LETTER</h2>
  </div>
  <article class="copy copy-interpret">
    <p>Most of the time the Reservation of Rights Letter is a generic form letter that states your insurance company is proceeding with handling your claim but reserves the right to deny coverage later on based upon any information that reveals reason to deny.</p>
    <p>Legitimate reasons an insurance company may deny coverage include when the loss occurred in relation to your retroactive date, specific exclusions in the policy language, prior knowledge of the incident, and coverage by another policy, among others.</p>
    <p class="lead-in">If the insurance company believes there may be reason for</p>
  </article>

  <article class="copy copy-right-top">
    <p>denial at the time the Reservation of Rights Letter is sent, it will be stated in the letter. For example, if the claim alleges breach of warranty, the letter will state that warranties are specifically excluded by the policy and it will include the policy language to demonstrate the exclusion.</p>
    <p>Even when specific reasons for potential coverage denial are cited, it is important to note that this is not a final verdict nor does it mean complete lack of coverage. Generally the insurance company is obligated to help you if any of your claims are covered by your insurance policy – there is a duty to defend. In cases such as the scenario above, circumstances of the claim will influence what is covered and what may be subject to exclusion.</p>
    <p>Based on investigative conclusions, the insurance company may not be obligated to pay the damages for certain types or aspects of claims.</p>
  </article>

  <div class="section-tab tab-proceed">
    <svg width="252" height="42" viewBox="0 0 252 42"><polygon points="0,0 252,0 252,42 0,42 18,21" fill="var(--brand-red)"/></svg>
    <h2>HOW TO PROCEED</h2>
  </div>
  <article class="copy copy-proceed">
    <p>Although the intent of the Reservation of Rights Letter is to protect the insurance company’s interests, it also alerts the policy holder to the fact that some elements of a claim may not be covered and therefore allows the insured to take steps to protect its potentially uninsured interests.</p>
    <p>However, receiving the Reservation of Rights Letter and even the insurance company’s interpretation of the policy language or law that they believe points toward coverage declination does not mean that you are automatically required to accept a denial of coverage.</p>
    <p>The best thing to do upon receiving the letter is to contact your broker and work closely with them and the insurance company claims handling department to ensure the prompt and fair handling of your claim.</p>
  </article>

  <footer>
    <svg class="footer-band" width="848" height="89" viewBox="0 0 848 89">
      <polygon points="80,0 768,0 784,36 64,36" fill="var(--brand-red)"/>
      <rect x="0" y="36" width="848" height="36" fill="var(--footer-dark)"/>
      <polygon points="0,72 848,72 824,89 24,89" fill="var(--brand-red)"/>
    </svg>
    <div class="footer-address">
      <svg width="13" height="18" viewBox="0 0 13 18"><path d="M6.5 0C2.9 0 0 2.9 0 6.5 0 11 6.5 18 6.5 18S13 11 13 6.5C13 2.9 10.1 0 6.5 0zm0 9.2a2.7 2.7 0 1 1 0-5.4 2.7 2.7 0 0 1 0 5.4z" fill="#fff"/></svg>
      <span>4821 Cedar Point Road NE, Kingsport, WA 98301</span>
    </div>
    <div class="footer-contacts">
      <div class="contact contact-phone">
        <svg width="16" height="16" viewBox="0 0 24 24"><path d="M6.6 10.8a15.1 15.1 0 0 0 6.6 6.6l2.2-2.2c.3-.3.7-.4 1-.2 1.1.4 2.3.6 3.6.6.6 0 1 .4 1 1V20c0 .6-.4 1-1 1C10.6 21 3 13.4 3 4c0-.6.4-1 1-1h3.5c.6 0 1 .4 1 1 0 1.3.2 2.5.6 3.6.1.3 0 .7-.2 1z" fill="none" stroke="#fff" stroke-width="2"/></svg>
        <span>555.014.3700</span>
      </div>
      <div class="contact contact-fax">
        <svg width="19" height="17" viewBox="0 0 19 17"><rect x="5" y="0.8" width="9" height="4.5" fill="none" stroke="#fff" stroke-width="1.6"/><rect x="0.8" y="5.3" width="17.4" height="7.5" rx="1" fill="#fff"/><rect x="5" y="10" width="9" height="6.2" fill="#fff" stroke="var(--footer-dark)" stroke-width="1.4"/></svg>
        <span>555.014.3703</span>
      </div>
      <div class="contact contact-web">
        <svg width="17" height="17" viewBox="0 0 20 20"><g fill="none" stroke="#fff" stroke-width="1.6"><circle cx="10" cy="10" r="8.6"/><ellipse cx="10" cy="10" rx="3.8" ry="8.6"/><path d="M1.6 10h16.8M3 5.5h14M3 14.5h14"/></g></svg>
        <span>www.kestrelriskadvisors.com</span>
      </div>
    </div>
  </footer>

</main>
</body>
</html>
```